Comercial & residential carpenter-Property maintanence

Hi, The II at the end of the company (R&T construction II) name is the roman numeral for the number 2 it was the only way i could have that business name, so i was thinking of incorporating the lettering for the business name with the latin alphabet to give some of that old world charm and some how try to show that my work will stand the test of time. Ive also come up with some ideas for slogans, Im not sure if they are any good.
Building the ideas of tomorrow today
Building not just a home but a lifestyle,your lifestyle
Built to stand the test of time
Not just a home but an extention of you
Building a better tomorrow for today

I work in the building and construction industry in Adelaide South Australia as a carpenter.

Industry/Entity Type

Construction

Contact Information for Business Card

Ironbark Joinery Co.
Robert Tomas Veld-DuMarais
ABN: 83 472 915 604
BLD: 517 389
PH: 0481 295 713
E Mail: pairmark@mailzone.com.au

```html
<!DOCTYPE html>
<html lang="en">
<head>
<meta charset="utf-8">
<title>Ironbark Joinery Co. – Business Card</title>
<link rel="stylesheet" href="https://fonts.googleapis.com/css2?family=Arimo:wght@400;700&display=swap">
<style>
  :root {
    --brown: #40210f;
    --orange: #f7962a;
    --paper: #ffffff;
    --edge: #8c8466;
  }
  * { box-sizing: border-box; margin: 0; padding: 0; }
  html, body {
    width: 1097px;
    height: 1200px;
    overflow: hidden;
    background: var(--paper);
    font-family: "Arimo", Arial, sans-serif;
  }
  .canvas { position: relative; width: 1097px; height: 1200px; }

  .card {
    position: absolute;
    left: 99px;
    width: 896px;
    height: 517px;
    border: 2px solid var(--edge);
    background: var(--paper);
    overflow: hidden;
  }
  .card--front { top: 41px; }
  .card--back { top: 655px; }

  /* Front */
  .stripe { position: absolute; top: 0; bottom: 0; }
  .stripe--brown { left: 36px; width: 47px; background: var(--brown); }
  .stripe--orange { left: 94px; width: 45px; background: var(--orange); }

  .brand {
    position: absolute;
    left: 180px;
    right: 30px;
    top: 214px;
    display: flex;
    align-items: center;
    justify-content: center;
    gap: 20px;
  }
  .brand__mark {
    width: 52px;
    height: 52px;
    border-radius: 50%;
    background: var(--orange);
    flex: none;
  }
  .brand__name {
    font-weight: 700;
    font-size: 50px;
    line-height: 60px;
    color: var(--brown);
    white-space: nowrap;
  }
  .slogan {
    position: absolute;
    left: 180px;
    right: 30px;
    top: 298px;
    text-align: center;
    font-weight: 700;
    font-size: 22px;
    color: var(--orange);
  }

  /* Back */
  .band--orange {
    position: absolute; left: 0; right: 0; top: 0; height: 206px;
    background: var(--orange);
  }
  .band--brown {
    position: absolute; left: 0; right: 0; top: 206px; height: 52px;
    background: var(--brown);
  }
  .holder {
    position: absolute; left: 0; right: 0; top: 172px;
    text-align: center;
    font-weight: 700;
    font-size: 27px;
    line-height: 32px;
    color: var(--brown);
  }
  .contact {
    position: absolute; left: 0; right: 0; top: 276px;
    text-align: center;
    color: var(--orange);
    font-size: 23px;
    line-height: 29px;
  }
  .contact__email {
    margin-top: 19px;
    font-weight: 700;
  }
</style>
</head>
<body>
<main class="canvas">
  <section class="card card--front" aria-label="Card front">
    <div class="stripe stripe--brown"></div>
    <div class="stripe stripe--orange"></div>
    <div class="brand">
      <span class="brand__mark" aria-hidden="true"></span>
      <span class="brand__name">Ironbark Joinery Co.</span>
    </div>
    <p class="slogan">Built to stand the test of time</p>
  </section>

  <section class="card card--back" aria-label="Card back">
    <div class="band--orange"></div>
    <div class="band--brown"></div>
    <p class="holder">Robert Tomas Veld-DuMarais</p>
    <div class="contact">
      <p>ABN: 83 472 915 604</p>
      <p>BLD: 517 389</p>
      <p>PH: 0481 295 713</p>
      <p class="contact__email">E Mail: pairmark@mailzone.com.au</p>
    </div>
  </section>
</main>
</body>
</html>
```